Research, Writing and Editing business needs a Business Card Design

I need a business card design for a new company based in Melbourne called The Amber Advisory Collective. We provide research, writing and editing services. The company logo is attached, but I am open to your creative designs for business cards with the logo. As you will note, there are two potential logos. Feel free to use either of the logos.

The overall look I am hoping for is sleek, sophisticated, feminine and elegant.

Thanks in advance for your efforts.

Target Market(s)

Business professionals, academics and students

Industry/Entity Type

Business

Font styles to use
Serif
Script

Colors

Designer to choose colors to be used in the design.

Requirements
Must have
• The Amber Advisory Collective
Dr Nola Fenwick

M: 0482 593 247
E: nola@theamberadvisorycollective.com.au
W: theamberadvisorycollective.com.au
Nice to have
• Research | Writing | Editing

```html
<!DOCTYPE html>
<html lang="en">
<head>
<meta charset="utf-8">
<title>The Amber Advisory Collective – Business Card</title>
<link href="https://fonts.googleapis.com/css2?family=Cormorant+Garamond:wght@500&family=Poiret+One&family=Roboto:wght@300&display=swap" rel="stylesheet">
<style>
  :root {
    --backdrop: #c9c9cd;
    --card-light: #fbfbfb;
    --card-mid: #e2e2e2;
    --card-shade: #cfcfcf;
    --ink: #141414;
    --ink-soft: #2a2a2a;
    --panel-text: #e8e8e8;
    --panel-muted: #bdbdbd;
  }
  * { box-sizing: border-box; margin: 0; padding: 0; }
  html, body {
    width: 1200px; height: 900px; overflow: hidden;
    background: var(--backdrop);
  }
  .canvas {
    position: relative; width: 1200px; height: 900px;
  }
  .card {
    position: absolute; left: 330px; width: 540px; height: 310px;
    overflow: hidden;
    background: linear-gradient(120deg, var(--card-light) 0%, var(--card-mid) 55%, var(--card-shade) 100%);
    box-shadow: 0 14px 30px rgba(0,0,0,.22);
  }
  .card--front { top: 110px; }
  .card--back  { top: 470px; }

  .brand {
    position: absolute; display: flex; align-items: center; gap: 10px;
    font-family: "Cormorant Garamond", Georgia, serif; font-weight: 500;
    color: var(--ink); line-height: 1.05;
  }
  .brand__dot {
    width: 12px; height: 12px; border-radius: 50%; background: var(--ink); flex: none;
  }
  .card--front .brand { left: 150px; top: 92px; font-size: 27px; }
  .card--back .brand { left: 372px; top: 92px; font-size: 19px; width: 160px; }

  .services-bar {
    position: absolute; left: 0; top: 196px; width: 390px; height: 44px;
    background: linear-gradient(180deg, var(--ink-soft), var(--ink));
    border-radius: 0 16px 16px 0;
    display: flex; align-items: center; justify-content: flex-end; padding-right: 24px;
    font-family: "Roboto", Arial, sans-serif; font-weight: 300;
    font-size: 17px; color: var(--panel-text); letter-spacing: .3px;
  }

  .contact-panel {
    position: absolute; left: 0; top: 22px; width: 352px; height: 266px;
    background: linear-gradient(160deg, var(--ink-soft), var(--ink));
    border-radius: 0 42px 42px 0;
    padding: 58px 0 0 40px;
    color: var(--panel-text);
  }
  .contact-panel__name {
    font-family: "Poiret One", "Century Gothic", sans-serif;
    font-size: 25px; letter-spacing: 2px; text-transform: uppercase;
  }
  .contact-panel__rule {
    width: 218px; height: 1px; background: var(--panel-muted); margin: 12px 0 18px;
  }
  .contact-list { list-style: none; }
  .contact-list li {
    display: flex; align-items: center; gap: 9px; margin-bottom: 6px;
    font-family: "Roboto", Arial, sans-serif; font-weight: 300;
    font-size: 12px; color: var(--panel-muted);
  }
  .contact-list svg { width: 13px; height: 13px; flex: none; }
</style>
</head>
<body>
<main class="canvas">

  <section class="card card--front" aria-label="Business card front">
    <div class="brand"><span class="brand__dot"></span><span class="brand__name">The Amber Advisory Collective</span></div>
    <div class="services-bar">Research | Writing | Editing</div>
  </section>

  <section class="card card--back" aria-label="Business card back">
    <div class="contact-panel">
      <h1 class="contact-panel__name">Dr Nola Fenwick</h1>
      <div class="contact-panel__rule"></div>
      <ul class="contact-list">
        <li>
          <svg viewBox="0 0 13 13" aria-hidden="true"><rect x="3" y="0.5" width="7" height="12" rx="1.5" fill="none" stroke="#bdbdbd"/><circle cx="6.5" cy="10.3" r=".8" fill="#bdbdbd"/></svg>
          0482 593 247
        </li>
        <li>
          <svg viewBox="0 0 13 13" aria-hidden="true"><rect x="0.5" y="2.5" width="12" height="8" fill="none" stroke="#bdbdbd"/><path d="M0.5 2.5 L6.5 7 L12.5 2.5" fill="none" stroke="#bdbdbd"/></svg>
          nola@theamberadvisorycollective.com.au
        </li>
        <li>
          <svg viewBox="0 0 13 13" aria-hidden="true"><circle cx="6.5" cy="6.5" r="6" fill="none" stroke="#bdbdbd"/><ellipse cx="6.5" cy="6.5" rx="2.6" ry="6" fill="none" stroke="#bdbdbd"/><line x1="0.5" y1="6.5" x2="12.5" y2="6.5" stroke="#bdbdbd"/></svg>
          theamberadvisorycollective.com.au
        </li>
      </ul>
    </div>
    <div class="brand"><span class="brand__dot"></span><span class="brand__name">The Amber Advisory Collective</span></div>
  </section>

</main>
</body>
</html>
```